Design some Business Cards for Vornel Solutions

Please create some double sided business card designs for Vornel Solutions.They will be printed by plix so please ensure that their guidelines are followed:

http://uk.plixprint-example.com/help/faq/using-my-own-artwork.html

What we do and are about can be found on our website:

http://www.vornels-example.com.au.

Please ensure that you include an area for the following details:
- Name
- title
- email
- Mobile (cell phone)
- Web url

Please provide a photoshop compatible file that can be modified to cater for different staff. We will save the final file with our details and names etc. as a jpeg to suit the printers requirements.

(A photoshop version of our logo can be found attached. Please ensure it is used.)

```html
<!DOCTYPE html>
<html lang="en">
<head>
<meta charset="utf-8">
<title>Vornel Solutions – Business Cards</title>
<link rel="stylesheet" href="https://fonts.googleapis.com/css2?family=Open+Sans:wght@400;600;700&display=swap">
<style>
  :root {
    --blue: #4a8fd0;
    --blue-soft: #6aa3da;
    --purple: #55307f;
    --grey: #7d7d7d;
    --slate: #6b6b6b;
    --paper: #ffffff;
    --backdrop: #e6e7e8;
  }
  * { box-sizing: border-box; margin: 0; padding: 0; }
  html, body {
    width: 1077px;
    height: 1200px;
    overflow: hidden;
  }
  body {
    background: var(--backdrop);
    font-family: "Open Sans", Arial, sans-serif;
    display: flex;
    align-items: center;
    justify-content: center;
    gap: 12px;
  }
  .card {
    position: relative;
    width: 512px;
    height: 288px;
    background: var(--paper);
    box-shadow: 0 6px 8px rgba(0,0,0,0.35);
    overflow: hidden;
  }
  .brand {
    position: absolute;
    display: flex;
    align-items: center;
    gap: 10px;
  }
  .brand-dot {
    width: 38px;
    height: 38px;
    border-radius: 50%;
    background: var(--purple);
    flex: none;
  }
  .brand-name {
    font-weight: 700;
    font-size: 27px;
    line-height: 1.05;
    color: var(--blue);
  }
  .card-front .brand { left: 30px; top: 34px; }
  .card-back .brand { right: 40px; top: 112px; }

  .person { position: absolute; left: 32px; top: 148px; }
  .person-name {
    font-weight: 700;
    font-size: 15px;
    color: var(--blue);
    letter-spacing: 0.3px;
  }
  .person-title {
    font-size: 11px;
    color: var(--grey);
    margin-top: 1px;
  }
  .contacts {
    position: absolute;
    left: 32px;
    top: 204px;
    list-style: none;
  }
  .contacts li {
    display: flex;
    align-items: center;
    gap: 9px;
    font-size: 11px;
    color: var(--slate);
    height: 20px;
  }
  .contact-icon {
    width: 15px;
    height: 15px;
    flex: none;
  }
  .artwork {
    position: absolute;
    top: 0;
    width: 120px;
    height: 288px;
  }
  .artwork-front {
    right: 0;
    background: linear-gradient(90deg, var(--purple), var(--blue));
  }
  .artwork-back {
    left: 0;
    background: linear-gradient(90deg, var(--blue), var(--blue-soft));
  }
  .web-url {
    position: absolute;
    right: 120px;
    bottom: 26px;
    font-size: 11px;
    color: var(--slate);
  }
  .web-url b { color: var(--blue); font-weight: 400; }
</style>
</head>
<body>

  <section class="card card-front" aria-label="Business card front">
    <div class="brand">
      <span class="brand-dot"></span>
      <span class="brand-name">Vornel<br>Solutions</span>
    </div>

    <div class="person">
      <p class="person-name">JOHN DOE</p>
      <p class="person-title">Executive Director</p>
    </div>

    <ul class="contacts">
      <li>
        <svg class="contact-icon" viewBox="0 0 16 16" aria-hidden="true">
          <circle cx="8" cy="8" r="8" fill="#4a8fd0"/>
          <rect x="5.5" y="3.5" width="5" height="9" rx="1" fill="#fff"/>
          <rect x="6.5" y="4.8" width="3" height="5.2" fill="#4a8fd0"/>
        </svg>
        +61 400 555 018
      </li>
      <li>
        <svg class="contact-icon" viewBox="0 0 16 16" aria-hidden="true">
          <circle cx="8" cy="8" r="8" fill="#4a8fd0"/>
          <rect x="4" y="5" width="8" height="6" fill="#fff"/>
          <path d="M4 5 L8 8.5 L12 5" fill="none" stroke="#4a8fd0" stroke-width="1"/>
        </svg>
        enquire@vornels-example.com.au
      </li>
      <li>
        <svg class="contact-icon" viewBox="0 0 16 16" aria-hidden="true">
          <circle cx="8" cy="8" r="8" fill="#4a8fd0"/>
          <circle cx="8" cy="8" r="4.3" fill="none" stroke="#fff" stroke-width="1"/>
          <ellipse cx="8" cy="8" rx="1.8" ry="4.3" fill="none" stroke="#fff" stroke-width="0.9"/>
          <line x1="3.7" y1="8" x2="12.3" y2="8" stroke="#fff" stroke-width="0.9"/>
        </svg>
        www.vornels-example.com.au
      </li>
    </ul>

    <div class="artwork artwork-front" role="img" aria-label="Brand illustration, left half"></div>
  </section>

  <section class="card card-back" aria-label="Business card back">
    <div class="artwork artwork-back" role="img" aria-label="Brand illustration, right half"></div>

    <div class="brand">
      <span class="brand-dot"></span>
      <span class="brand-name">Vornel<br>Solutions</span>
    </div>

    <p class="web-url">www.<b>vornels-example</b>.com.au</p>
  </section>

</body>
</html>
```